Byteway Tech Services Flyer

I have a retail Computer Store that I want to promote in the local area.
The target market is seniors aged between 40-80 year olds. I need to create a flyer for the business to do a flyer drop to homes and business advertising the business & services we offer. I would also like to drop this on our socials for online target ads.
Store Name: Byteway Tech systems Address: 17 Larkspur Road, ALDERVALE Westmere 3904 Phone Number: (03) 9521 6408 Target Audience: older generation between 40 - 90 year olds Services offered: Retail Sales & Service, Complete Workshop Facilities, Cloud services, Deskly 240 Experts, Network & Wireless Products, Managed Services, PC & Laptop Sales, Custom Built Computers Vendors: Veltrix, QORNL, Parvanix Partner, Olex, Brimo, KT & Rune Reseller Please keep it to A1 size and double sided with options to go A3 o A4 later.

Target Market(s)

Residential home users

Industry/Entity Type

www.bytewaytech.com.au

Font styles to use
Sans Serif

Colors
0054AA
0677BA
7BADD7
CADEEF
E8F1F8

Requirements
Must have
• Simple target is the elderly population

```html
<!DOCTYPE html>
<html lang="en">
<head>
<meta charset="utf-8">
<title>Byteway Tech Services Flyer</title>
<link href="https://fonts.googleapis.com/css2?family=Poppins:wght@400;500;600;700&display=swap" rel="stylesheet">
<style>
  :root {
    --brand-blue: #0054AA;
    --mid-blue: #0677BA;
    --soft-blue: #7BADD7;
    --pale-blue: #CADEEF;
    --ice-blue: #E8F1F8;
    --ink: #111722;
    --white: #ffffff;
    --backdrop: #e4e6ea;
  }
  html, body {
    margin: 0;
    padding: 0;
    width: 1200px;
    height: 2182px;
    overflow: hidden;
    background: var(--backdrop);
    font-family: "Poppins", sans-serif;
  }
  .flyer {
    position: absolute;
    left: 50px;
    top: 314px;
    width: 1100px;
    height: 1553px;
    display: block;
    box-shadow: 0 6px 24px rgba(0,0,0,0.18);
  }
  .flyer text { font-family: "Poppins", sans-serif; }
  .brand-name { fill: var(--brand-blue); font-weight: 600; font-size: 27px; letter-spacing: 1px; }
  .section-title { fill: var(--brand-blue); font-weight: 700; font-size: 23px; }
  .vendor-title { fill: var(--brand-blue); font-weight: 700; font-size: 21px; }
  .list-item { fill: var(--ink); font-weight: 600; font-size: 18.5px; }
  .headline { fill: var(--white); font-weight: 700; font-size: 46px; }
  .question { fill: var(--pale-blue); font-weight: 600; font-size: 21px; }
  .body-copy { fill: var(--white); font-weight: 400; font-size: 17.5px; }
  .info-small { fill: var(--soft-blue); font-weight: 400; font-size: 15px; }
  .info-strong { fill: var(--soft-blue); font-weight: 600; font-size: 17.5px; }
  .info-line { fill: var(--soft-blue); font-weight: 400; font-size: 18px; }
  .phone { fill: var(--soft-blue); font-weight: 700; font-size: 27px; }
</style>
</head>
<body>
<svg class="flyer" viewBox="0 0 932 1316" xmlns="http://www.w3.org/2000/svg">
  <defs>
    <linearGradient id="paperTone" x1="0" y1="0" x2="0" y2="1">
      <stop offset="0" stop-color="#ffffff"/>
      <stop offset="1" stop-color="#E8F1F8"/>
    </linearGradient>
    <linearGradient id="photoTone" x1="0" y1="0" x2="1" y2="1">
      <stop offset="0" stop-color="#1b5f95"/>
      <stop offset="0.5" stop-color="#1a3f7a"/>
      <stop offset="1" stop-color="#3b2f6a"/>
    </linearGradient>
    <clipPath id="paperClip"><rect width="932" height="1316"/></clipPath>
  </defs>

  <g clip-path="url(#paperClip)">
    <rect class="paper" width="932" height="1316" fill="url(#paperTone)"/>

    <path class="info-panel" d="M466 760 L466 420 L932 200 L932 1278 L466 1191 Z" fill="var(--brand-blue)"/>
    <polygon class="corner-accent" points="820,1278 932,1278 932,1316 870,1316" fill="var(--soft-blue)"/>
    <circle class="photo-ring" cx="466" cy="262" r="468" fill="url(#paperTone)"/>

    <circle class="hero-photo" cx="466" cy="262" r="436" fill="url(#photoTone)" role="img" aria-label="Photo of hands fitting a component into a computer motherboard, lit in blue"/>
  </g>

  <rect class="brand-mark" x="37" y="728" width="36" height="36" rx="6" fill="var(--mid-blue)"/>
  <text class="brand-name" x="84" y="757">Byteway Tech systems</text>

  <text class="section-title" x="37" y="841">SERVICES OFFERED:</text>
  <g class="list-item">
    <text x="70" y="880">•  Retail Sales &amp; Service</text>
    <text x="70" y="918">•  Complete Workshop Facilities</text>
    <text x="70" y="955">•  Cloud services</text>
    <text x="70" y="993">•  Deskly 240 Experts</text>
    <text x="70" y="1030">•  Network &amp; Wireless Products</text>
    <text x="70" y="1068">•  Managed Services</text>
    <text x="70" y="1105">•  PC &amp; Laptop Sales</text>
  </g>

  <text class="vendor-title" x="37" y="1168">Custom Built Computers Vendors:</text>
  <g class="list-item">
    <text x="70" y="1201">•  Veltrix</text>
    <text x="70" y="1234">•  Parvanix Partner</text>
    <text x="70" y="1267">•  Brimo</text>
    <text x="295" y="1201">•  QORNL</text>
    <text x="295" y="1234">•  Olex</text>
    <text x="295" y="1267">•  KT &amp; Rune Reseller</text>
  </g>

  <text class="headline" x="508" y="792">NEW COMPUTER</text>
  <text class="question" x="508" y="844">Don’t know where to start....?</text>
  <text class="question" x="508" y="869">Don’t know what you need....?</text>
  <g class="body-copy">
    <text x="508" y="908">Want to keep up with the latest in</text>
    <text x="508" y="929">technology? We can help you. Whether you</text>
    <text x="508" y="950">are a small or medium business, run a</text>
    <text x="508" y="971">home office, or are a passionate “Gamer”,</text>
    <text x="508" y="992">we can come up with the perfect solution to</text>
    <text x="508" y="1013">your computer needs.</text>
  </g>
  <text x="508" y="1053"><tspan class="info-small">STORE MON - FRI  -  </tspan><tspan class="info-strong">9:00 AM - 5:30 PM</tspan></text>
  <text class="info-line" x="508" y="1090">17 Larkspur Road, ALDERVALE Westmere 3904</text>
  <text class="info-small" x="508" y="1134">Need Help? Phone Number:</text>
  <text class="phone" x="508" y="1164">(03) 9521 6408</text>
</svg>
</body>
</html>
```